Tennly Packaging Business Card

Project Overview
We are seeking a modern, minimalist business card that effectively represents our company while making a bold and lasting impression. The design should reflect trust, professionalism, and innovation, reinforcing our expertise in custom plastic manufacturing for warehouse and distribution centers.

Provided Assets & Specifications
Logo: We will provide our official logo for integration into the design.
Design Files: Photoshop (PSD) files for our printing specifications will be supplied.

Card Size & Material:
Dimensions: 3.5" x 2"
Material: 1/8" Radius Plastic Business Cards with 1/8" Rounded Corners
Clear plastic background—the design should strategically incorporate transparency.
Orientation: The card should be designed in landscape format for a sleek and professional presentation.

Design Requirements:
Logo Prominence
The logo must be the focal point of the card.
Space should be used effectively to draw attention to the logo while maintaining a minimalist layout.

Clear Plastic Integration
The transparent background should create the illusion of blank space, enhancing the modern and high-quality feel.
Avoid any frosted effects—we do not want white areas to appear semi-transparent.

Minimalist & Impactful
Clean, structured, and easy to read at a glance.
Focus on sharp contrast to ensure legibility and visibility.
The design should instill confidence and reflect our role as a leading plastics manufacturer.

Color Palette & Contrast
Primary Colors: Blue, Black, White, and Grey
Use bold black or blue for text and key elements to ensure they stand out against the clear plastic.
Avoid light, pastel, or neon colors that may fade into the plastic background.
No frosted or semi-transparent white—we do not want a cloudy effect.

Typography & Information Hierarchy
Bold, modern typography—clear, professional, and highly legible.
The business card should highlight:
Company Logo (Primary Focus)
Full Name & Title
Phone Number
Email
Website

Brand Representation
The card should reflect our expertise in manufacturing high-quality custom plastics for large-scale packaging and distribution businesses.
Our clients rely on us to enhance their brand presence through custom plastic solutions, and our business cards should reinforce that sense of precision and trust.

Final Considerations
Utilize the clear plastic effectively to differentiate our brand from standard business cards.
Maintain a sleek, professional aesthetic while ensuring all text and elements remain legible.
The design should align with our industry, conveying reliability and innovation.
We look forward to seeing a design that captures our brand identity, maximizes the clear plastic medium, and makes a strong, professional impact on our clients.

```html
<!DOCTYPE html>
<html lang="en">
<head>
<meta charset="utf-8">
<title>Tennly Packaging Business Card</title>
<link href="https://fonts.googleapis.com/css2?family=Roboto:wght@400;500;700&display=swap" rel="stylesheet">
<style>
  :root {
    --page-bg: #9aa4a6;
    --card-clear: #d9dcdc;
    --ink: #2f2f31;
    --brand-blue: #1b8fc6;
    --rule: #2f2f31;
    --ghost: rgba(255,255,255,0.55);
  }
  * { margin: 0; padding: 0; box-sizing: border-box; }
  html, body {
    width: 1200px; height: 1181px; overflow: hidden;
    background: var(--page-bg);
    font-family: "Roboto", Arial, sans-serif;
  }
  .canvas { position: relative; width: 1200px; height: 1181px; }
  .card {
    position: absolute;
    width: 700px; height: 400px;
    border-radius: 24px;
    background: var(--card-clear);
    box-shadow: 0 14px 30px rgba(0,0,0,0.18);
    overflow: hidden;
  }
  .card-front { left: 70px; top: 110px; }
  .card-back { left: 430px; top: 650px; }

  .holder { position: absolute; left: 44px; top: 42px; }
  .holder-name { font-size: 30px; font-weight: 700; color: var(--ink); line-height: 1; }
  .holder-title { font-size: 19px; font-weight: 400; color: var(--brand-blue); margin-top: 6px; }
  .holder-rule { width: 100px; height: 1.5px; background: var(--rule); margin-top: 8px; }
  .contacts { list-style: none; margin-top: 14px; }
  .contacts li {
    display: flex; align-items: center; gap: 7px;
    font-size: 18px; color: var(--ink); line-height: 26px;
  }
  .contacts svg { width: 15px; height: 15px; flex: none; }

  .wordmark {
    position: absolute; left: 44px; bottom: 48px;
    display: flex; align-items: center; gap: 12px;
    font-size: 40px; font-weight: 700; color: var(--brand-blue); line-height: 1;
  }
  .wordmark .mark-square { width: 34px; height: 34px; background: var(--ink); }

  .feature-name {
    position: absolute; right: 60px; top: 150px;
    font-size: 80px; font-weight: 700; color: var(--brand-blue); line-height: 1;
  }

  .mirror { transform: scaleX(-1); }
  .ghost-side { position: absolute; inset: 0; }
  .ghost-side .holder { left: 36px; top: 30px; }
  .ghost-side .holder-name { font-size: 24px; font-weight: 500; color: var(--ghost); }
  .ghost-side .holder-title { font-size: 16px; color: var(--ghost); }
  .ghost-side .holder-rule { background: var(--ghost); width: 120px; }
  .ghost-side .contacts li { font-size: 16px; line-height: 24px; color: var(--ghost); }
  .ghost-side .wordmark { left: 44px; bottom: 48px; font-size: 40px; color: var(--ghost); }
  .ghost-side .wordmark .mark-square { background: var(--ghost); width: 60px; height: 60px; }

  .back-feature {
    position: absolute; left: 60px; top: 150px;
    font-size: 80px; font-weight: 700; color: var(--brand-blue); line-height: 1;
  }
</style>
</head>
<body>
<main class="canvas">

  <section class="card card-front" aria-label="Card front">
    <div class="holder">
      <p class="holder-name">Marcus Ellery</p>
      <p class="holder-title">Sales Manager</p>
      <div class="holder-rule"></div>
      <ul class="contacts">
        <li>
          <svg viewBox="0 0 16 16" aria-hidden="true"><circle cx="8" cy="8" r="8" fill="#2f2f31"/><path d="M5 4.5l1.6-.4.9 2-1 .8a5 5 0 0 0 2.6 2.6l.8-1 2 .9-.4 1.6c-3.7.3-6.8-2.8-6.5-6.5z" fill="#d9dcdc"/></svg>
          +01 55512 04817
        </li>
        <li>
          <svg viewBox="0 0 16 16" aria-hidden="true"><circle cx="8" cy="8" r="8" fill="#2f2f31"/><rect x="4" y="5" width="8" height="6" rx="1" fill="#d9dcdc"/><path d="M4 5.5l4 3 4-3" stroke="#2f2f31" stroke-width="1" fill="none"/></svg>
          marcusellery@mailbox.com
        </li>
        <li>
          <svg viewBox="0 0 16 16" aria-hidden="true"><circle cx="8" cy="8" r="8" fill="#2f2f31"/><circle cx="8" cy="8" r="4.5" fill="none" stroke="#d9dcdc" stroke-width="1"/><path d="M3.5 8h9M8 3.5c-2 2.5-2 6.5 0 9M8 3.5c2 2.5 2 6.5 0 9" stroke="#d9dcdc" stroke-width="0.9" fill="none"/></svg>
          www.tennlypackaging.com
        </li>
      </ul>
    </div>
    <p class="feature-name">Tennly</p>
    <div class="wordmark"><span class="mark-square"></span>Tennly Packaging</div>
  </section>

  <section class="card card-back" aria-label="Card back, front printing visible through the clear plastic">
    <div class="ghost-side mirror">
      <div class="holder">
        <p class="holder-name">Marcus Ellery</p>
        <p class="holder-title">Sales Manager</p>
        <div class="holder-rule"></div>
        <ul class="contacts">
          <li>+01 55512 04817</li>
          <li>marcusellery@mailbox.com</li>
          <li>www.tennlypackaging.com</li>
        </ul>
      </div>
      <div class="wordmark"><span class="mark-square"></span>Tennly Packaging</div>
    </div>
    <p class="back-feature">Tennly</p>
  </section>

</main>
</body>
</html>
```